lantern institute of business and technology web site

I need web site for the institute which focus on business courses and computer course it is also for vocation train for employment It is also carear development and advancement .It should have links to online study resource which free
Industry/Entity Type
Business
Number of Pages Required
1 page
Look and feel

```html
<!DOCTYPE html>
<html lang="en">
<head>
<meta charset="utf-8">
<title>Lantern Institute of Business and Technology</title>
<link href="https://fonts.googleapis.com/css2?family=Open+Sans:wght@400;600;700&family=Roboto:wght@400;500;700&display=swap" rel="stylesheet">
<style>
:root{
  --blue:#1f9be0;
  --blue-dark:#1d66b3;
  --navy:#1b2a57;
  --band:#233d85;
  --green:#2eae3e;
  --orange:#f29b1c;
  --ink:#222;
  --muted:#666;
  --white:#fff;
  --footer:#17234a;
  --footer-deep:#0f1834;
}
*{box-sizing:border-box;margin:0;padding:0}
html,body{width:1200px;height:2540px;overflow:hidden}
body{font-family:"Open Sans",Arial,sans-serif;color:var(--ink);background:var(--white);position:relative}
a{color:inherit;text-decoration:none}
ul{list-style:none}

.site-header{position:absolute;top:0;left:0;width:1200px;height:60px;background:var(--white);z-index:3}
.brand-box{position:absolute;left:40px;top:0;width:180px;height:140px;background:var(--blue-dark);display:flex;flex-direction:column;align-items:center;justify-content:center;gap:8px;z-index:4;color:var(--white);text-align:center}
.brand-box .mark{width:44px;height:44px;border-radius:50%;background:var(--white)}
.brand-box .name{font-size:12px;font-weight:700;line-height:1.25;text-transform:uppercase}
.main-nav{position:absolute;right:140px;top:20px;display:flex;gap:22px;font-size:13px;font-weight:600;color:#444}
.main-nav .active{color:var(--blue);border-bottom:2px solid var(--blue);padding-bottom:4px}
.social-top{position:absolute;right:40px;top:20px;display:flex;gap:8px}
.social-top span{width:16px;height:16px;border-radius:50%;background:#888}

.hero{position:absolute;top:60px;left:0;width:1200px;height:440px;background:linear-gradient(100deg,#6a4a7a 0%,#c9b7a4 35%,#e5ddd2 55%,#8a5a4a 80%,#4a3a3a 100%)}

.program-bar{position:absolute;top:500px;left:0;width:1200px;height:40px;background:var(--blue);display:flex;justify-content:flex-end;align-items:center;gap:34px;padding-right:60px;color:var(--white);font-size:12px;font-weight:700;text-transform:uppercase}

.tagline{position:absolute;top:596px;left:0;width:1200px;text-align:center;font-family:Roboto,Arial,sans-serif;font-size:36px;font-weight:500;line-height:1.3;color:#1a1a1a;text-transform:uppercase}

.courses-intro{position:absolute;top:760px;left:70px;width:620px}
.courses-intro h2{font-family:Roboto,Arial,sans-serif;font-size:28px;font-weight:500;line-height:1.2;text-transform:uppercase;color:#111}
.courses-intro p{margin-top:16px;font-size:13px;line-height:1.5;color:var(--muted)}
.courses-intro h3{margin-top:18px;font-size:15px;font-weight:700;color:var(--blue-dark);text-transform:uppercase}
.program-list{margin-top:14px;display:grid;grid-template-columns:1fr 1fr;row-gap:12px;font-size:14px;color:var(--blue-dark)}
.program-list li::before{content:"";display:inline-block;width:7px;height:7px;background:var(--blue);margin-right:8px;vertical-align:middle}
.helpdesk{margin-top:28px;display:flex;align-items:center;gap:16px}
.helpdesk .label{font-size:15px;font-weight:700;line-height:1.2;text-transform:uppercase;color:#111}
.helpdesk .numbers{font-size:14px;font-weight:600;line-height:1.4;color:#333}

.feature-grid{position:absolute;top:760px;left:740px;width:400px;height:420px;display:grid;grid-template-columns:1fr 1fr;grid-template-rows:1fr 1fr;gap:4px}
.feature{color:var(--white);display:flex;flex-direction:column;align-items:center;justify-content:center;text-align:center;padding:14px}
.feature h4{margin-top:12px;font-size:13px;font-weight:700;text-transform:uppercase}
.feature p{margin-top:6px;font-size:11px;line-height:1.4}
.feature.blue{background:var(--blue)}
.feature.green{background:var(--green)}
.feature.navy{background:var(--navy)}
.feature.orange{background:var(--orange)}

.highlights{position:absolute;top:1240px;left:0;width:1200px;height:760px;background:var(--band)}
.highlight-grid{position:absolute;top:90px;left:60px;width:1080px;height:580px;display:grid;grid-template-columns:repeat(3,1fr);grid-template-rows:1fr 1fr;gap:10px}
.tile{color:var(--white);display:flex;flex-direction:column;align-items:center;justify-content:center;text-align:center;padding:24px 30px}
.tile h4{font-size:16px;font-weight:700;text-transform:uppercase}
.tile p{margin-top:14px;font-size:12px;line-height:1.5}
.tile .more{margin-top:14px;font-size:11px;font-weight:700;text-transform:uppercase}
.tile.blue{background:var(--blue)}
.tile.green{background:var(--green)}
.tile.orange{background:var(--orange)}
.tile.photo-graduates{background:linear-gradient(160deg,#e8eef5,#9aa9bd 60%,#2b2b2b)}
.tile.photo-library{background:linear-gradient(160deg,#7a5a3a,#c69a62 50%,#e6d2b4)}
.tile.photo-student{background:linear-gradient(160deg,#9cc7d8,#d9a79a 50%,#3b6e3c)}

.partners{position:absolute;top:2040px;left:0;width:1200px;height:100px;display:flex;justify-content:center;align-items:center;gap:70px;color:#333}
.partner{display:flex;align-items:center;gap:10px;font-size:16px;font-weight:700;text-transform:uppercase}
.partner .badge{width:30px;height:30px;background:#555}

.site-footer{position:absolute;top:2180px;left:0;width:1200px;height:360px;background:var(--footer);color:#c8d0e6}
.footer-brand{position:absolute;left:90px;top:70px;width:200px;text-align:center;color:var(--white)}
.footer-brand .mark{width:70px;height:70px;border-radius:50%;background:#3a4a80;margin:0 auto 12px}
.footer-brand .name{font-size:13px;font-weight:700;line-height:1.3;text-transform:uppercase}
.footer-col{position:absolute;top:40px;width:180px}
.footer-col h5{font-size:14px;font-weight:700;color:var(--white);text-transform:uppercase;margin-bottom:14px}
.footer-col li{font-size:11px;line-height:2.2;text-transform:uppercase}
.col-quick{left:370px}.col-academics{left:560px}.col-campus{left:760px}.col-connect{left:960px}
.connect li{display:flex;align-items:center;gap:8px;text-transform:none;font-size:12px}
.connect li span{width:12px;height:12px;border-radius:50%;background:var(--blue)}
.copyright{position:absolute;bottom:0;left:0;width:1200px;height:40px;background:var(--footer-deep);padding:8px 60px;font-size:10px;line-height:1.4;color:#9aa4c2;text-transform:uppercase}
</style>
</head>
<body>

<header class="site-header">
  <nav class="main-nav">
    <a class="active" href="#">Home</a><a href="#">About Us</a><a href="#">Courses</a><a href="#">Apply Online</a><a href="#">Self Help</a><a href="#">Contact</a>
  </nav>
  <div class="social-top"><span></span><span></span><span></span></div>
</header>
<div class="brand-box">
  <span class="mark"></span>
  <span class="name">Lantern Institute of<br>Business &amp; Technology</span>
</div>

<div class="hero" role="img" aria-label="Two students studying with books and notes in a library"></div>

<nav class="program-bar">
  <a href="#">Under Graduate Programs</a><a href="#">Master Degree Programs</a><a href="#">Post Graduate Programs</a><a href="#">IT Courses</a><a href="#">Diploma Courses</a>
</nav>

<h1 class="tagline">Teamwork enhances productivity, performance<br>and skill development</h1>

<section class="courses-intro">
  <h2>Our popular IT<br>and business courses</h2>
  <p>Learn practical business and computer skills with flexible schedules, expert tutors and free online study resources that prepare you for employment and career growth.</p>
  <h3>Popular programs &amp; courses</h3>
  <ul class="program-list">
    <li>Under Graduate Programs</li><li>Diploma Programs</li>
    <li>Master Degree Programs</li><li>Advanced Diploma Programs</li>
    <li>Post Graduate Programs</li><li>Finance &amp; Accounting Courses</li>
    <li>Certificate Level Programs</li><li>Medical Information Technology (IT)</li>
  </ul>
  <div class="helpdesk">
    <svg width="34" height="34" viewBox="0 0 24 24"><path fill="#1b2a57" d="M6.6 10.8a15 15 0 0 0 6.6 6.6l2.2-2.2c.3-.3.7-.4 1-.2 1.1.4 2.3.6 3.6.6.6 0 1 .4 1 1V20c0 .6-.4 1-1 1A17 17 0 0 1 3 4c0-.6.4-1 1-1h3.5c.6 0 1 .4 1 1 0 1.3.2 2.5.6 3.6.1.3 0 .7-.2 1z"/></svg>
    <div class="label">Office<br>Helpdesk</div>
    <div class="numbers">555-014-2880<br>555-019-9321</div>
  </div>
</section>

<section class="feature-grid">
  <div class="feature blue">
    <svg width="40" height="40" viewBox="0 0 40 40"><rect x="6" y="4" width="28" height="32" fill="none" stroke="#fff" stroke-width="3"/><line x1="12" y1="14" x2="28" y2="14" stroke="#fff" stroke-width="3"/><line x1="12" y1="22" x2="28" y2="22" stroke="#fff" stroke-width="3"/></svg>
    <h4>Business Courses</h4><p>Courses designed to boost your career and development</p>
  </div>
  <div class="feature green">
    <svg width="40" height="40" viewBox="0 0 40 40"><rect x="4" y="6" width="32" height="22" fill="none" stroke="#fff" stroke-width="3"/><line x1="14" y1="34" x2="26" y2="34" stroke="#fff" stroke-width="3"/></svg>
    <h4>IT Courses</h4><p>Courses designed to boost your career and development</p>
  </div>
  <div class="feature navy">
    <svg width="40" height="40" viewBox="0 0 40 40"><circle cx="20" cy="20" r="15" fill="none" stroke="#fff" stroke-width="3"/><circle cx="20" cy="20" r="6" fill="#fff"/></svg>
    <h4>Targeted Audience</h4><p>Courses designed to boost your career and development</p>
  </div>
  <div class="feature orange">
    <svg width="40" height="40" viewBox="0 0 40 40"><path d="M8 24v-4a12 12 0 0 1 24 0v4" fill="none" stroke="#fff" stroke-width="3"/><rect x="5" y="22" width="7" height="10" fill="#fff"/><rect x="28" y="22" width="7" height="10" fill="#fff"/></svg>
    <h4>Technical Support</h4><p>Courses designed to boost your career and development</p>
  </div>
</section>

<section class="highlights">
  <div class="highlight-grid">
    <div class="tile blue">
      <h4>Excellent Training</h4>
      <p>Hands-on lessons led by experienced trainers help you build workplace skills and gain confidence for your next job.</p>
      <a class="more" href="#">Click here to know more</a>
    </div>
    <div class="tile photo-graduates" role="img" aria-label="Graduates in caps and gowns celebrating"></div>
    <div class="tile orange">
      <h4>Anytime Anywhere</h4>
      <p>Study at your own pace with free online resources, recorded lectures and course notes available on any device.</p>
      <a class="more" href="#">Click here to know more</a>
    </div>
    <div class="tile photo-library" role="img" aria-label="Student reading among library shelves"></div>
    <div class="tile green">
      <h4>Digital Technology</h4>
      <p>Modern computer labs and current software tools give learners real practice with the technology employers use.</p>
      <a class="more" href="#">Click here to know more</a>
    </div>
    <div class="tile photo-student" role="img" aria-label="Smiling student holding books outdoors"></div>
  </div>
</section>

<section class="partners">
  <div class="partner"><span class="badge"></span>Westmoor University</div>
  <div class="partner"><span class="badge"></span>Coral Bay University</div>
  <div class="partner"><span class="badge"></span>Harbor Crest University</div>
  <div class="partner"><span class="badge"></span>SkillBridge</div>
  <div class="partner"><span class="badge"></span>Westmoor University</div>
</section>

<footer class="site-footer">
  <div class="footer-brand">
    <div class="mark"></div>
    <div class="name">Lantern Institute of<br>Business &amp; Technology</div>
  </div>
  <div class="footer-col col-quick">
    <h5>Quick Links</h5>
    <ul><li>Home</li><li>About Us</li><li>Courses</li><li>Apply Online</li><li>Self Help</li><li>Contact Us</li></ul>
  </div>
  <div class="footer-col col-academics">
    <h5>Academics</h5>
    <ul><li>Course Application Forms</li><li>Exam Dates</li><li>Application Deadline</li><li>Study Materials</li><li>Library</li><li>Event Calendar</li></ul>
  </div>
  <div class="footer-col col-campus">
    <h5>Campus</h5>
    <ul><li>Campus Information</li><li>Digital IT Policy</li><li>Terms &amp; Conditions</li><li>Students Desk</li><li>Office Help</li><li>Contacts</li></ul>
  </div>
  <div class="footer-col col-connect connect">
    <h5>Get Connected</h5>
    <ul><li><span></span>Community Page</li><li><span></span>Short Updates</li><li><span></span>Circles Page</li><li><span></span>Video Channel</li></ul>
  </div>
  <div class="copyright">Copyright 2024. All rights reserved.<br>Terms &amp; conditions · Privacy · Disclaimer</div>
</footer>

</body>
</html>
```